Delivery Docket urgent plus require many other designs for more stationary after this.

We need a new delivery docket design urgently as the one we have needs updating and we have changed our company name. Please do not copy the one I have uploaded as we do not feel this looks professional enough. I uploaded it as a few designers requested to see what we are currently using thank you.
It is quite complex in that we need a range of information to be on the one docket.
We are a Transport Company based in Australia that has a wide variety of items that we deliver such as water, sand and gravels and heavy equipment transport.
We would prefer to keep this design to A5 size as we will get them made into books. We are looking for a modern professional look. Although it is only a delivery docket this is given to all our customers so needs to look impressive.

We need our new logo on the docket (PRW). There will also need to be areas for our address and contact numbers, email etc these will be supplied to the winning designer to make the final adjustments so for now just put something generic in these spaces.
Needs to have an area for customer details, purchase order number, date and docket number (docket number to be in red)
Needs a section where we can list the type of product / and or service that has been provided and the amount / qty usually 3 lines will be enough for this. Need area under this where the customer can sign name and print name to say that the goods / and or services have been received.

Also required somewhere on the docket are the words, Tax Invoice will be issued based on the information provided on this docket. Conditions on back of page

We then need a separate section on the same page which we will use internally that the staff member can tear off and hand into the office. On this section it needs to have area where the driver can list km at start of job and at end with space to calculate km travelled, details of fuel purchased eg amount and litres, vehicle that is being used. also need to log down wheel bearing temps.
prime mover needs spaces as follows
Steer axel FL____________ Steer axel FR _________ 1st drive axel L_______
1st drive axel R_________ 2nd drive axel L_______ 2nd drive axel R________

For the trailers need something similar x 2 as have 2 trailers
1st axel DS_________ 1st axel PS_________ 2nd axel DS__________
2nd axel PS_________ 3rd axel DS_________ 3rd axel PS__________

I have included a few examples of designs we have used in past and ones that we like so you can get an idea of the colours we prefer, I have included some of the designs we are currently receiving for our logo that I like so you can get idea again of colours we prefer. There is much more we need designed also such as time sheets, more delivery dockets and letter heads so there is a lot of more work available to the winning designer.

Thank you

Target Market(s)

Customers

Font styles to use
Serif
Sans Serif

Colors

Designer to choose colors to be used in the design.

Requirements
Should not have
• Please don't copy old docket as we do not like it and nned new info on new design thank you

```html
<!DOCTYPE html>
<html lang="en">
<head>
<meta charset="utf-8">
<title>PRW Delivery Docket</title>
<link rel="stylesheet" href="https://fonts.googleapis.com/css2?family=Cabin:wght@400;700&display=swap">
<style>
  :root {
    --backdrop: #3a3a3a;
    --paper: #ffffff;
    --red: #e8313a;
    --ink: #1c1c1c;
    --black: #151515;
    --grey-dark: #5a5a5a;
    --rule: #444444;
    --watermark: #eeeeee;
  }
  * { box-sizing: border-box; margin: 0; padding: 0; }
  html, body { width: 1200px; height: 1200px; overflow: hidden; }
  body {
    background: var(--backdrop);
    font-family: "Cabin", sans-serif;
    color: var(--ink);
    position: relative;
  }
  .docket {
    position: absolute; left: 40px; top: 140px;
    width: 1120px; height: 920px;
    background: var(--paper);
  }
  .abs { position: absolute; }

  .title-tab {
    left: 70px; top: 95px; width: 300px; height: 48px;
    background: var(--red); color: #fff;
    font-weight: 700; font-size: 27px; letter-spacing: .5px;
    display: flex; align-items: center; justify-content: center;
  }
  .head-rule { left: 370px; top: 95px; width: 500px; height: 1px; background: var(--red); }
  .head-field { font-weight: 700; font-size: 20px; top: 109px; }
  .invoice-no { left: 400px; }
  .docket-number { color: var(--red); margin-left: 6px; letter-spacing: 1px; }
  .date { left: 660px; }

  .brand {
    right: 40px; top: 40px;
    font-weight: 700; font-size: 96px; line-height: 1; color: var(--black);
    letter-spacing: 2px;
  }

  .outer-frame { left: 70px; top: 143px; width: 1040px; height: 745px; border: 1px solid var(--rule); border-top: none; }

  .field { display: flex; align-items: flex-end; gap: 8px; font-weight: 700; font-size: 16px; white-space: nowrap; }
  .field .line { flex: 1; border-bottom: 1px solid var(--rule); height: 1px; margin-bottom: 4px; min-width: 40px; }

  .vehicle-row { left: 80px; top: 160px; width: 620px; display: flex; gap: 16px; }
  .vehicle-row .field:first-child { flex: 1.4; }
  .vehicle-row .field { flex: 1; }

  .fuel-rule { left: 80px; top: 200px; width: 620px; height: 1px; background: var(--rule); }
  .divider-v { left: 700px; top: 143px; width: 1px; height: 140px; background: var(--rule); }

  .contact {
    left: 700px; top: 170px; width: 410px;
    text-align: center; font-size: 15px; line-height: 1.35; font-style: normal;
  }

  .customer-box { left: 100px; top: 208px; width: 600px; height: 78px; }
  .customer-grid { position: absolute; inset: 4px 10px; display: grid; grid-template-columns: 1fr 1.3fr; row-gap: 6px; column-gap: 16px; }
  .customer-grid .wide { grid-column: 1 / 3; }

  .tear-line { left: 0; top: 292px; width: 1120px; border-top: 2px dashed var(--grey-dark); }
  .tear-label {
    right: 12px; top: 274px;
    font-size: 12px; font-weight: 700; color: var(--grey-dark); letter-spacing: .6px;
  }

  .temps-band {
    left: 90px; top: 304px; width: 1020px; height: 42px;
    background: var(--red); color: #fff;
    font-weight: 700; font-size: 21px; letter-spacing: .5px;
    display: flex; align-items: center; justify-content: center;
  }
  .temps-box { left: 90px; top: 346px; width: 1020px; height: 136px; border: 1px solid var(--red); border-top: none; }
  .temps-grid {
    position: absolute; inset: 8px 16px;
    display: grid; grid-template-columns: 1.35fr 1fr 1.35fr 1fr;
    row-gap: 6px; column-gap: 18px;
  }
  .temps-grid .field { font-size: 15px; }

  .log-table {
    left: 100px; top: 492px; width: 1000px;
    border-collapse: collapse; table-layout: fixed;
  }
  .log-table th {
    background: var(--black); color: #fff;
    font-weight: 700; font-size: 17px; height: 32px; letter-spacing: .4px;
  }
  .log-table th.description { background: linear-gradient(90deg, var(--grey-dark), var(--black)); }
  .log-table td { height: 27px; border: 1px solid var(--rule); }
  .col-qty { width: 62px; }
  .col-desc { width: 548px; }
  .col-km { width: 130px; }

  .watermark {
    left: 330px; top: 560px;
    font-weight: 700; font-size: 200px; line-height: 1; color: var(--watermark);
    letter-spacing: 8px;
  }

  .sign-row { left: 100px; top: 808px; width: 1000px; display: flex; gap: 40px; }
  .sign-row .field { flex: 1; }

  .tax-note {
    left: 70px; top: 852px; width: 1040px;
    text-align: center; font-size: 14px; font-weight: 700;
  }
  .tax-note .conditions { color: var(--red); }
</style>
</head>
<body>
  <main class="docket">
    <div class="abs title-tab">DELIVERY DOCKET</div>
    <div class="abs head-rule"></div>
    <div class="abs head-field invoice-no">INVOICE NO.:<span class="docket-number">000001</span></div>
    <div class="abs head-field date">DATE:</div>
    <div class="abs brand">PRW</div>

    <div class="abs outer-frame"></div>

    <div class="abs vehicle-row">
      <div class="field">Vehicle Used <span class="line"></span></div>
      <div class="field">Fuel added in Litres <span class="line"></span></div>
      <div class="field">Cost of fuel <span class="line"></span></div>
    </div>
    <div class="abs fuel-rule"></div>
    <div class="abs divider-v"></div>

    <address class="abs contact">
      Your address goes here<br>
      Contact No. : 000000000<br>
      Web: mail@prwtransport.com
    </address>

    <section class="abs customer-box">
      <div class="customer-grid">
        <div class="field wide">Name: <span class="line"></span></div>
        <div class="field">Order No.: <span class="line"></span></div>
        <div class="field">Delivery Item: <span class="line"></span></div>
        <div class="field wide">Delivery Address: <span class="line"></span></div>
      </div>
    </section>

    <div class="abs tear-line" aria-hidden="true"></div>
    <div class="abs tear-label">OFFICE COPY – DRIVER TO TEAR OFF</div>

    <div class="abs temps-band">WHEEL BEARING TEMPS</div>
    <section class="abs temps-box">
      <div class="temps-grid">
        <div class="field">Prime mover Steer axel FL <span class="line"></span></div>
        <div class="field">Steer axel FR <span class="line"></span></div>
        <div class="field">1st drive axel L <span class="line"></span></div>
        <div class="field">1st drive axel R <span class="line"></span></div>

        <div class="field">2nd drive axel L <span class="line"></span></div>
        <div class="field">2nd drive axel R <span class="line"></span></div>
        <div class="field">Lead Trailer 1st axel DS <span class="line"></span></div>
        <div class="field">1st axel PS <span class="line"></span></div>

        <div class="field">2nd axel DS <span class="line"></span></div>
        <div class="field">2nd axel PS <span class="line"></span></div>
        <div class="field">3rd axel DS <span class="line"></span></div>
        <div class="field">3rd axel PS <span class="line"></span></div>

        <div class="field">Second Trailer 1st axel DS <span class="line"></span></div>
        <div class="field">1st axel PS <span class="line"></span></div>
        <div class="field">2nd axel DS <span class="line"></span></div>
        <div class="field">2nd axel PS <span class="line"></span></div>

        <div class="field">3rd axel DS <span class="line"></span></div>
        <div class="field">3rd axel PS <span class="line"></span></div>
      </div>
    </section>

    <div class="abs watermark" aria-hidden="true">PRW</div>

    <table class="abs log-table">
      <colgroup>
        <col class="col-qty"><col class="col-desc"><col class="col-km"><col class="col-km"><col class="col-km">
      </colgroup>
      <thead>
        <tr><th>QTY</th><th class="description">DESCRIPTION</th><th>START KM</th><th>END KM</th><th>TOTAL KM</th></tr>
      </thead>
      <tbody>
        <tr><td></td><td></td><td></td><td></td><td></td></tr>
        <tr><td></td><td></td><td></td><td></td><td></td></tr>
        <tr><td></td><td></td><td></td><td></td><td></td></tr>
        <tr><td></td><td></td><td></td><td></td><td></td></tr>
        <tr><td></td><td></td><td></td><td></td><td></td></tr>
        <tr><td></td><td></td><td></td><td></td><td></td></tr>
        <tr><td></td><td></td><td></td><td></td><td></td></tr>
        <tr><td></td><td></td><td></td><td></td><td></td></tr>
        <tr><td></td><td></td><td></td><td></td><td></td></tr>
      </tbody>
    </table>

    <div class="abs sign-row">
      <div class="field">Goods Received by (Print Name) <span class="line"></span></div>
      <div class="field">Signed <span class="line"></span></div>
    </div>

    <p class="abs tax-note">Tax Invoice will be issued based on the information provided on this docket. <span class="conditions">Conditions on back of page</span></p>
  </main>
</body>
</html>
```